Mobile Spray tanner needs a Mobile Spray tanning business card design

I need a simple but eye-catching business card design. I would like the business card to be in two colours only (Hot pink background with black Silhouette & black writing). I would like the white behind the silhouette removed and the other bits on the silhouette removed (to be just a black silhouette with a hot pink bikini on). I would like the black writing to be aesthetically pleasing and quite artistic, but easy to read). Thank you very much

```html
<!DOCTYPE html>
<html lang="en">
<head>
<meta charset="utf-8">
<title>Golden Glow – Mobile Spray Tanning Business Card</title>
<link href="https://fonts.googleapis.com/css2?family=Oranienbaum&display=swap" rel="stylesheet">
<style>
  :root {
    --page-bg: #e6e6e6;
    --hot-pink: #e0119a;
    --hot-pink-deep: #a30070;
    --ink: #111111;
    --band: #141414;
    --band-edge: #2a2a2a;
    --white: #ffffff;
  }
  * { box-sizing: border-box; margin: 0; padding: 0; }
  html, body {
    width: 1200px;
    height: 941px;
    overflow: hidden;
    background: var(--page-bg);
  }
  .canvas {
    position: relative;
    width: 1200px;
    height: 941px;
    display: flex;
    align-items: center;
    justify-content: center;
  }
  .business-card {
    position: relative;
    width: 470px;
    height: 760px;
    background: radial-gradient(ellipse at 50% 35%, var(--hot-pink) 0%, var(--hot-pink) 45%, var(--hot-pink-deep) 100%);
    box-shadow: 0 12px 30px rgba(0,0,0,0.25);
    overflow: hidden;
    font-family: "Oranienbaum", "Times New Roman", serif;
  }
  .brand-name {
    position: absolute;
    top: 58px;
    left: 0;
    right: 0;
    text-align: center;
    color: var(--ink);
    font-size: 64px;
    letter-spacing: 1px;
    line-height: 1;
  }
  .figure-silhouette {
    position: absolute;
    top: 150px;
    left: 120px;
    width: 230px;
    height: 330px;
    border-radius: 110px 110px 30px 30px;
    background: linear-gradient(180deg, #1a1a1a 0%, #000000 100%);
  }
  .service-line {
    position: absolute;
    top: 500px;
    left: 0;
    right: 0;
    text-align: center;
    color: var(--ink);
    font-size: 38px;
    letter-spacing: 1px;
    line-height: 1;
  }
  .contact-band {
    position: absolute;
    left: 0;
    right: 0;
    bottom: 0;
    height: 168px;
    background: linear-gradient(180deg, var(--band-edge) 0%, var(--band) 30%, #050505 100%);
    display: flex;
    align-items: center;
    justify-content: center;
    gap: 18px;
  }
  .phone-icon { width: 34px; height: 34px; }
  .phone-number {
    color: var(--white);
    font-size: 50px;
    letter-spacing: 1px;
    line-height: 1;
  }
</style>
</head>
<body>
  <main class="canvas">
    <article class="business-card">
      <h1 class="brand-name">GOLDEN GLOW</h1>
      <div class="figure-silhouette" role="img" aria-label="Black silhouette of a kneeling woman wearing a hot pink bikini"></div>
      <p class="service-line">MOBILE SPRAY TANNING</p>
      <div class="contact-band">
        <svg class="phone-icon" viewBox="0 0 34 34" aria-hidden="true">
          <circle cx="17" cy="17" r="17" fill="#ffffff"/>
          <path d="M11 9.5c1-.8 2.2-.6 2.8.4l1.4 2.4c.5.9.3 1.8-.5 2.4l-1 .7c.8 1.9 2.3 3.6 4.2 4.6l.8-1c.6-.8 1.6-1 2.4-.5l2.4 1.4c1 .6 1.1 1.9.3 2.8l-1.2 1.3c-1.3 1.3-4.4.9-7.6-2.2s-4.2-6.4-3.1-8.2z" fill="#141414"/>
        </svg>
        <span class="phone-number">0400123987</span>
      </div>
    </article>
  </main>
</body>
</html>
```